Looking for new banner ad to use in online magazine advertisements

We are looking for design ideas for a few ads we need to publish in online magazines. We are a plumbing distributor that specializes in backflow repair parts. Our web page is www.drainkitdepot.com which shows the products and manufacturers we sell. We are looking for an ad that can be displayed in a few different size formats so please send over your ideas for each size listed below.
We are redesigning our website and we have a test site up were you can get a look at the design we are going with as well as pull photos and images from. The web addresss for our new site is http://pipeline.stagehollow.com/

We need to have an ad that is 600 x 100, 120 x 500, and a half page ad that would be 600 x 200

I have attached a few of the print flyers we are using at this point so you can have an idea of past designs we have gone with.

Industry/Entity Type

Distribution

Requirements
Must have
• We need to have an ad that is 600 x 100, 120 x 500, and a half page ad that would be 600 x 200
• 600 w x 100 h
• 120 w x 500 h
• 600 w x 200 h
Nice to have
• See webpages below for images and design ideas.
• Old website: www.drainkitdepot.com
• New web page: http://pipeline.stagehollow.com/

```html
<!DOCTYPE html>
<html lang="en">
<head>
<meta charset="utf-8">
<title>Gauge Calibration Banner</title>
<link rel="stylesheet" href="https://fonts.googleapis.com/css2?family=Arimo:wght@400;700&display=swap">
<style>
  :root {
    --ink: #111111;
    --accent-red: #c8102e;
    --brand-navy: #1f2f6b;
    --paper: #ffffff;
    --gauge-light: #f4f4f2;
    --gauge-mid: #c9cbcc;
    --gauge-dark: #5d6266;
  }
  * { margin: 0; padding: 0; box-sizing: border-box; }
  html, body {
    width: 1200px;
    height: 200px;
    overflow: hidden;
    background: var(--paper);
  }
  .banner {
    position: relative;
    width: 1200px;
    height: 200px;
    overflow: hidden;
    background: var(--paper);
    font-family: "Arimo", Arial, sans-serif;
    color: var(--ink);
  }
  .price-ribbon {
    position: absolute;
    left: 0;
    top: 0;
    width: 170px;
    height: 170px;
  }
  .headline {
    position: absolute;
    left: 180px;
    top: 16px;
    font-size: 51px;
    font-weight: 700;
    letter-spacing: -0.3px;
    white-space: nowrap;
  }
  .tagline {
    position: absolute;
    left: 180px;
    top: 80px;
    font-size: 36px;
    font-weight: 400;
    white-space: nowrap;
  }
  .call-to-action {
    position: absolute;
    left: 180px;
    top: 138px;
    font-size: 31px;
    color: var(--accent-red);
    white-space: nowrap;
  }
  .call-to-action .cta-label { font-weight: 700; }
  .call-to-action .cta-phone { font-weight: 400; }
  .brand {
    position: absolute;
    left: 664px;
    top: 134px;
    display: flex;
    align-items: center;
    gap: 12px;
    color: var(--brand-navy);
  }
  .brand-mark {
    width: 28px;
    height: 28px;
    background: var(--brand-navy);
  }
  .brand-name {
    font-size: 22px;
    font-weight: 400;
    line-height: 1.1;
  }
  .gauge-photo {
    position: absolute;
    left: 965px;
    top: -34px;
    width: 310px;
    height: 310px;
    border-radius: 50%;
    background: radial-gradient(circle at 45% 45%, var(--gauge-light) 0%, var(--gauge-light) 58%, var(--gauge-mid) 66%, var(--gauge-dark) 74%, var(--gauge-mid) 82%, var(--gauge-dark) 100%);
  }
</style>
</head>
<body>
  <div class="banner">
    <svg class="price-ribbon" viewBox="0 0 170 170" aria-label="Only $98.99">
      <polygon points="0,20 20,0 160,0 0,160" fill="var(--accent-red)"/>
      <g transform="translate(52 52) rotate(-45)" fill="#ffffff" font-family="Arimo, Arial, sans-serif" font-weight="700" text-anchor="middle">
        <text x="0" y="-12" font-size="22">ONLY</text>
        <text x="0" y="18" font-size="30">$98.99</text>
      </g>
    </svg>

    <h1 class="headline">Hassle Free Gauge Calibration</h1>
    <p class="tagline">Easy, quick &amp; affordable</p>
    <p class="call-to-action"><span class="cta-label">BOOK TODAY</span> <span class="cta-phone">(800) 555 0142</span></p>

    <div class="brand">
      <span class="brand-mark"></span>
      <span class="brand-name">Crestline Valve<br>Supply</span>
    </div>

    <div class="gauge-photo" role="img" aria-label="Photo of a round differential pressure test gauge with white dial"></div>
  </div>
</body>
</html>
```